I need bigcommerce design template

hi, am looking for a quality, professional, attractive and mature bigcommerce template for my site. My site will sell clothes and bags and shoes. Basically what you are to do is setup the store. I have domain name which hostwren will attach them self.

```html
<!DOCTYPE html>
<html lang="en">
<head>
<meta charset="utf-8">
<title>Store Template</title>
<link rel="stylesheet" href="https://fonts.googleapis.com/css2?family=Arimo:wght@400;700&family=Comfortaa:wght@300;400;700&family=Share+Tech+Mono&family=Space+Mono:wght@700&display=swap">
<style>
:root{
  --page:#ffffff;
  --pink:#d8285e;
  --pink-dark:#a42350;
  --mauve:#7a3f55;
  --mauve-soft:#8a4c62;
  --ink:#555;
  --grey:#888;
  --yellow:#ffe11a;
  --footer:#222222;
  --footer-text:#8a8a8a;
  --card-line:#c8285c;
  --button:#b51c4d;
}
*{margin:0;padding:0;box-sizing:border-box}
html,body{width:1200px;height:900px;overflow:hidden;background:var(--page)}
body{position:relative;font-family:"Arimo",sans-serif}
.abs{position:absolute}
.top-strip{left:212px;top:0;width:775px;height:13px;background:linear-gradient(#f05a85,var(--pink) 40%,#8e1d44);border-bottom:1px solid #6a1634}
.top-strip span{position:absolute;top:3px;width:30px;height:8px;border-radius:50%;background:radial-gradient(#fff,rgba(255,255,255,0) 70%)}
.logo{left:251px;top:28px;font-family:"Comfortaa",sans-serif;color:#6b6b6b;line-height:1}
.logo .l1{font-size:19px}
.logo .l2{font-size:13px}
.util-links{top:45px;right:253px;display:flex;gap:11px;font-size:10px;font-weight:700;color:var(--grey)}
.sidebar{left:212px;top:64px;width:140px;height:234px;background:linear-gradient(90deg,#b7244f,#e33a6c 15%,#c42a58 60%,#a8234d)}
.side-panel{left:238px;top:88px;width:111px;height:210px;border-radius:10px 10px 0 0;background:linear-gradient(180deg,#8f2448,#b22e58 40%,#c03462);box-shadow:inset 2px 2px 4px rgba(0,0,0,.35)}
.side-menu{left:264px;top:101px;list-style:none;font-family:"Space Mono",monospace;font-size:8.5px;color:#fff;line-height:13px}
.side-menu .active{color:var(--yellow)}
.nav{left:352px;top:64px;width:635px;height:30px;background:var(--mauve);display:flex;align-items:center;justify-content:space-around;padding:0 10px 0 4px;font-family:"Space Mono",monospace;font-size:12.5px;color:#fff}
.hero{left:352px;top:94px;width:635px;height:204px;background:linear-gradient(90deg,#8d8789,#d8d2d3 40%,#3a3335 48%,#2a2426 54%,#b9b3b4 62%,#7d7779)}
.news{left:212px;top:298px;width:775px;height:111px;background:var(--mauve)}
.news-title{left:232px;top:305px;width:114px;text-align:right;font-family:"Comfortaa",sans-serif;color:#fff;line-height:21px}
.news-title .big{font-size:23px}
.news-title .small{font-size:18px}
.more{font-size:8.5px;font-weight:700;color:#d48aa4}
.news-more{left:311px;top:388px}
.news-text{top:309px;width:276px;font-family:"Share Tech Mono",monospace;font-size:9.4px;line-height:13.4px;color:#efdfe4;height:92px;overflow:hidden}
.news-divider{left:654px;top:298px;width:2px;height:111px;background:#fff}
.sec-head{top:409px;height:29px;background:linear-gradient(90deg,var(--pink-dark),#d45b83 45%,#f6dde6 80%,#fff);font-family:"Share Tech Mono",monospace;font-size:17px;color:#fff;padding:4px 0 0 17px;letter-spacing:1px}
.sec-more{top:419px;color:#9a7a85}
.stars{left:234px;top:412px;width:106px;height:210px;background:linear-gradient(180deg,#e8e8e8,#f4f4f4 60%,#fff)}
.vdivider{left:652px;top:462px;width:1px;height:291px;background:#aaa}
.card{width:138px;height:143px;border:1.5px solid var(--card-line);background:#fff;text-align:center}
.card .photo{position:absolute;left:37px;top:20px;width:64px;height:72px;border-radius:6px}
.ring{background:radial-gradient(circle at 50% 40%,#d880c8,#5fb6d6 40%,#c9cfd6 65%,#fff 80%)}
.bag{background:linear-gradient(#3a8ed0,#1e64a8)}
.frock{background:linear-gradient(#e0323a,#b81e24)}
.card .name{position:absolute;left:0;right:0;top:106px;font-size:7.5px;color:#666}
.card .btn{position:absolute;left:43px;top:122px;width:51px;height:13px;background:var(--button);color:#fff;font-size:7.5px;line-height:13px}
.footer{left:212px;top:780px;width:775px;height:120px;background:var(--footer)}
.fcol{top:797px;font-size:6.5px;color:var(--footer-text);line-height:12.7px}
.fcol h4{color:#fff;font-size:6.5px;font-weight:700;margin-bottom:3px}
.fcol.contact{line-height:9.6px}
.signup{display:flex;margin-top:2px}
.signup .field{width:78px;height:15px;background:#fff;border:1px solid #999;color:#777;font-size:6px;padding:3px 2px}
.signup .go{width:32px;height:15px;background:var(--button);color:#fff;font-size:6.5px;line-height:15px;text-align:center}
.social{display:flex;gap:5px;margin-top:3px}
.social span{width:19px;height:19px;border-radius:50%}
</style>
</head>
<body>
<div class="abs top-strip"><span style="left:240px"></span><span style="left:377px"></span><span style="left:510px"></span><span style="left:645px"></span></div>

<div class="abs logo"><div class="l1">Your</div><div class="l2">Company LOGO</div></div>
<div class="abs util-links"><span>Home</span><span>Contact</span><span>Sitemap</span></div>

<div class="abs sidebar"></div>
<div class="abs side-panel"></div>
<ul class="abs side-menu">
  <li class="active">INTRODUCTION</li><li>YOUR MATTERS</li><li>YOUR MATTERS</li><li>YOUR MATTERS</li><li>YOUR MATTERS</li>
</ul>

<nav class="abs nav"><span>HOME</span><span>PRODUCTS</span><span>NEW</span><span>BEST SELLER</span><span>SPECILAS</span><span>CONTACT US</span></nav>

<div class="abs hero" role="img" aria-label="Black-and-white city street photo with a woman in a black coat carrying colourful shopping bags"></div>

<section class="abs news"></section>
<div class="abs news-title"><div class="big">What's</div><div class="small">News</div></div>
<div class="abs more news-more">+ MORE</div>
<p class="abs news-text" style="left:371px">Lorem Ipsum is simply dummy text of the printing and type-setting industry. Lorem Ipsum has been the industry's standard dummy text ever since the 1500s, when an unknown printer took a galley of type and scrambled it to make a type specimen book. It has survived not only five centuries, but also the leap into electronic typesetting, remaining essentially unchanged. It was popularised in the 1960s with</p>
<div class="abs news-divider"></div>
<p class="abs news-text" style="left:675px">Lorem Ipsum is simply dummy text of the printing and type-setting industry. Lorem Ipsum has been the industry's standard dummy text ever since the 1500s, when an unknown printer took a galley of type and scrambled it to make a type specimen book. It has survived not only five centuries, but also the leap into electronic typesetting, remaining essentially unchanged. It was popularised in the 1960s with</p>

<div class="abs stars" role="img" aria-label="Faint grey star pattern fading downward"></div>

<h2 class="abs sec-head" style="left:352px;width:288px;font-weight:400">BIG DEALS</h2>
<div class="abs more sec-more" style="left:607px">+ MORE</div>
<h2 class="abs sec-head" style="left:654px;width:301px;font-weight:400">POPULAR PRODUCTS</h2>
<div class="abs more sec-more" style="left:921px">+ MORE</div>

<div class="abs vdivider"></div>

<div class="abs card" style="left:359px;top:460px"><div class="photo ring" role="img" aria-label="Ring product photo"></div><div class="name">Ring</div><div class="btn">Add to Cart</div></div>
<div class="abs card" style="left:506px;top:460px"><div class="photo bag" role="img" aria-label="Blue handbag product photo"></div><div class="name">Violet</div><div class="btn">Add to Cart</div></div>
<div class="abs card" style="left:665px;top:460px"><div class="photo frock" role="img" aria-label="Red frock product photo"></div><div class="name">Frock</div><div class="btn">Add to Cart</div></div>
<div class="abs card" style="left:812px;top:460px"><div class="photo frock" role="img" aria-label="Red frock product photo"></div><div class="name">Frock</div><div class="btn">Add to Cart</div></div>
<div class="abs card" style="left:359px;top:619px"><div class="photo ring" role="img" aria-label="Ring product photo"></div><div class="name">Ring</div><div class="btn">Add to Cart</div></div>
<div class="abs card" style="left:506px;top:619px"><div class="photo bag" role="img" aria-label="Blue handbag product photo"></div><div class="name">Violet</div><div class="btn">Add to Cart</div></div>
<div class="abs card" style="left:665px;top:619px"><div class="photo ring" role="img" aria-label="Ring product photo"></div><div class="name">Ring</div><div class="btn">Add to Cart</div></div>
<div class="abs card" style="left:812px;top:619px"><div class="photo ring" role="img" aria-label="Ring product photo"></div><div class="name">Ring</div><div class="btn">Add to Cart</div></div>

<footer class="abs footer"></footer>
<div class="abs fcol" style="left:297px"><h4>INFORMATION</h4><div>ABOUT US</div><div>DELIVERY INFORMATION</div><div>PRIVACY POLICY</div><div>TERMS &amp; CONDITIONS</div></div>
<div class="abs fcol" style="left:452px"><h4>MY ACCOUNT</h4><div>MY ACCOUNT</div><div>VIEW CART</div><div>CHECKOUT</div><div>SIGN IN / REGISTER</div></div>
<div class="abs fcol contact" style="left:608px"><h4>CONTACT US</h4><div>48 Alder Row,</div><div>20917 Brookfield</div><div>+ 000 555 0142</div><div>hello@shopmail.test</div></div>
<div class="abs fcol" style="left:764px"><h4>SIGN UP FOR EMAILS</h4>
  <div class="signup"><div class="field">Email address</div><div class="go">Submit</div></div>
  <h4 style="margin-top:12px">FOLLOW US</h4>
  <div class="social"><span style="background:#3b5998"></span><span style="background:#3aa3e3"></span><span style="background:#8a6d55"></span><span style="background:#d34836"></span><span style="background:#d9322b"></span></div>
</div>
</body>
</html>
```